Frost Leaf: CBD and Herbal Topical Pain product needs a brochure

We need a brochure that educates customers on the product. The product combines traditional Chinese herbs used for pain and swelling with a strong dose of CBD to apply topical with a glass, roll-on applicator. We would like to see dark blue as a dominant color or anything ice related. The logo is an iceberg but doesn't need to be included.

Target Market(s)

Cannabis Dispensaries, Chiro, Acu offices,
Health / Wellness, Alternative Medicine

Industry/Entity Type

Alternative Medicine

Colors
0455a3

Requirements
Must have
• Frost Leaf
• 500mg CBD in 1oz
• For: Muscle, Joint Pain, Swelling, Acute Injuries, Chronic Pain, Arthritis
• Directions: Apply a thin layer of herbal formula over the affected area. Apply as needed.
• Caution: Avoid hot water shortly after application.
• Ingredients: Angelica Root, Camphor, Cannabidoil (CBD), Cinnamon, Dandelion, Gardenia, Ginger, Licorice, Menthol, Myrrh, Phellodendron Bark, Rhubarb, Safflower, Sesame Oil, Scutellaria
• Highlight amount of CBD: 500mg
• Secondary highlights it includes Turmeric and Magnesium
• Easy Roll-On Topical Pain Relief for Muscle Spasms, Joint Pain, Strains, Sprains, Swelling
• Increases circulation to increase recovery time. Great for athletes
• Stops pain by numbing painful, slower deep nerve signals by stimulating the faster, superficial nerves with a cooling sensation
• Reduce painful swelling and heat involved with inflammation.
• Breaks up damaged tissue to enhance the natural healing process
• Ingredients
• Dang Gui – Angelica : reduces swelling, generates tissue, alleviates pain, expels pus
• Cinnamon –Gui Zhi decreases arthritic pain
• Carthamus Flower / safflower –Hong Hua - reduces swelling, alleviates pain,
• Rhubarb – Da Huang -bruising, acute and chronic swelling
• Licorice –Gan Cao - alleviates spasms, anti-inflammatory
• Phellodendron Huang Bai– reduces swelling and pain
• Dandelion – Pu Gong Ying – reduces swelling and nodules, anti-inflammatory
• Mo Yao – Myrrh – reduces swelling, pain, bruising, and masses, promotes healing
• Ginger – Gan Jiang – chronic swelling, increases circulation
• Gardenia – Zhi Zi- Reduces swelling from trauma, bruising
• Scutellaria – Huang Qin – hot sores, swelling,
• Magnesium – helps muscle spasms
• Camphor – mild, local anesthetic effect, alleviates pain, pain and swelling from sprains
• Menthol – rashes, swelling, relaxes muscles
• Turmeric – reduces inflammation and swelling
• Sesame Oil – carrier oil
• Cannabidiol (CBD) Isolate
• Colloidal Silver (Natural Preservative)
• Formulated by a Herbalist and Doctor of Chinese Medicine, Dr. Wendell Prasky, DAOM
Nice to have
• Iceberg or ice theme
• Copy:
• Frost Leaf blends traditional Chinese herbs with a potent dose of hemp derived cannabidiol (CBD) isolate. Instantly feel the cooling icy sensation penetrate deep into sore muscles and joints to sooth away pain.
• Not only does the menthol give a temporary cooling effect which helps numb pain, the other herbal ingredients continue to soothe tight, achy muscles and joints. It can also be applied for an acute sprain or strain to reduce swelling, just like applying ice.
• Ice is used by athletes and recommended by doctors to reduce pain and swelling. Frost Leaf can reduce pain and swelling without having to carry a bag of ice around.
• With the easy roll-on application, you dont even have to get your hands cold!
• Traditional Chinese Medicine has used the same herbs for thousands of years to help ease the pain of injuries during battle. Herbal plasters, liniments, and oils were the most common application to maximize the healing benefits of the herbs. Frost Leaf uses organic, raw herbs which are ground into a fine powder and further extracted in sesame oil. Once extracted, the oil is filtered and then CBD is then added as the oil is cooling.
• Pictures of a few of the herbs - I have a few already if needed

```html
<!DOCTYPE html>
<html lang="en">
<head>
<meta charset="utf-8">
<title>Frost Leaf Brochure – Inside</title>
<link href="https://fonts.googleapis.com/css2?family=Montserrat:wght@500;700;800&family=Nunito+Sans:wght@400;600&family=PT+Sans+Narrow:wght@400;700&display=swap" rel="stylesheet">
<style>
  :root {
    --navy: #133d6b;
    --navy-deep: #0e2f58;
    --navy-panel: #112a55;
    --brand-blue: #0455a3;
    --gold: #f7b81f;
    --white: #ffffff;
    --ice: #dfe7ee;
    --herb-grey: #9aa3ab;
    --kitchen-white: #eef0f1;
  }
  * { box-sizing: border-box; margin: 0; padding: 0; }
  html, body { width: 1200px; height: 1200px; overflow: hidden; background: var(--white); }
  body { position: relative; font-family: "Nunito Sans", sans-serif; }

  .spread-label {
    position: absolute; top: 76px; left: 0; width: 1200px; text-align: center;
    font-family: "Montserrat", sans-serif; font-weight: 800; font-size: 66px;
    letter-spacing: 5px; color: var(--navy); line-height: 1;
  }

  .brochure {
    position: absolute; left: 30px; top: 159px; width: 1140px; height: 881px;
    background: radial-gradient(ellipse at 30% 40%, #1d4a7e 0%, var(--navy) 45%, var(--navy-deep) 100%);
    box-shadow: 0 3px 10px rgba(0,0,0,0.18);
    overflow: hidden; color: var(--white);
  }

  .copy {
    position: absolute; font-size: 14px; line-height: 26px;
    text-align: justify; font-weight: 600; letter-spacing: 0.2px;
  }
  .copy.bullet::before {
    content: ""; position: absolute; left: -19px; top: 8px;
    width: 9px; height: 9px; border-radius: 50%; background: var(--gold);
  }
  .copy-left { left: 44px; width: 330px; }

  .photo { position: absolute; }
  .photo-mortar { left: 0; top: 437px; width: 378px; height: 184px;
    background: linear-gradient(135deg, var(--kitchen-white) 0%, #dcdedf 55%, #b58a5a 100%); }
  .photo-spices { left: 746px; top: 73px; width: 382px; height: 574px;
    background: linear-gradient(160deg, #b7bec4 0%, var(--herb-grey) 45%, #a86a4a 80%, #c2412a 100%); }

  .band-blue { position: absolute; left: 746px; top: 0; width: 191px; height: 26px; background: var(--brand-blue); }
  .band-white { position: absolute; left: 937px; top: 0; width: 203px; height: 26px; background: #eef1f5; }

  .product-label {
    position: absolute; left: 454px; top: 490px; width: 216px; height: 204px;
    border-top: 2px solid var(--white); border-bottom: 2px solid var(--white);
    background: linear-gradient(180deg, transparent 0%, var(--navy-panel) 40%, var(--navy-panel) 100%);
    text-align: center;
  }
  .product-name { position: absolute; top: 10px; width: 100%;
    font-family: "PT Sans Narrow", sans-serif; font-weight: 700; font-size: 27px; }
  .product-type { position: absolute; top: 140px; width: 100%;
    font-family: "PT Sans Narrow", sans-serif; font-size: 17px; }
  .product-ingredients { position: absolute; top: 164px; width: 100%;
    font-family: "PT Sans Narrow", sans-serif; font-size: 9.5px; }
  .product-size { position: absolute; top: 182px; width: 100%;
    font-family: "PT Sans Narrow", sans-serif; font-size: 10px; }

  .contact { position: absolute; left: 400px; width: 340px; text-align: center; color: var(--gold);
    font-family: "Montserrat", sans-serif; }
  .contact-phone { top: 702px; font-weight: 700; font-size: 23px; letter-spacing: 0.5px; }
  .contact-address { top: 740px; font-weight: 500; font-size: 12.5px; line-height: 21px; }

  .title-box {
    position: absolute; left: 746px; top: 709px; width: 394px; height: 105px;
    background: var(--brand-blue); text-align: center;
    font-family: "Montserrat", sans-serif; font-weight: 700; font-size: 36px; line-height: 43px;
    padding-top: 10px;
  }
  .title-box .accent { color: var(--gold); }

  .ice-ridge { position: absolute; left: 0; top: 760px; width: 1140px; height: 121px;
    background: linear-gradient(180deg, rgba(223,231,238,0) 0%, rgba(223,231,238,0.55) 45%, var(--ice) 100%); }
</style>
</head>
<body>
  <h1 class="spread-label">INSIDE</h1>

  <section class="brochure">
    <div class="ice-ridge" role="img" aria-label="Row of icy white glacier peaks along the bottom edge"></div>

    <p class="copy copy-left bullet" style="top:67px;">Frost Leaf blends traditional Chinese herbs with a potent dose of hemp derived cannabidiol (CBD) isolate. Instantly feel the cooling icy sensation penetrate deep into sore muscles and joints to sooth away pain.</p>
    <p class="copy copy-left bullet" style="top:249px;">Not only does the menthol give a temporary cooling effect which helps numb pain, the other herbal ingredients continue to soothe tight, achy muscles and joints. It can also be applied for an acute sprain or strain to reduce swelling, just like applying ice.</p>

    <div class="photo photo-mortar" role="img" aria-label="White mortar and pestle with fresh herbs, garlic, turmeric and peppercorns on a wooden board"></div>

    <p class="copy copy-left bullet" style="top:637px; width:333px;">Ice is used by athletes and recommended by doctors to reduce pain and swelling. Frost Leaf can reduce pain and swelling without having to carry a bag of ice around.</p>
    <p class="copy copy-left bullet" style="top:766px; width:333px;">With the easy roll-on application, you dont even have to get your hands cold!</p>

    <p class="copy" style="left:414px; top:67px; width:296px;">Traditional Chinese Medicine has used the same herbs for thousands of years to help ease the pain of injuries during battle. Herbal plasters, liniments, and oils were the most common application to maximize the healing benefits of the herbs. Frost Leaf uses organic, raw herbs which are ground into a fine powder and further extracted in sesame oil. Once extracted, the oil is filtered and then CBD is then added as the oil is cooling.</p>

    <div class="product-label">
      <div class="product-name">Frost Leaf</div>
      <div class="product-type">Pain Relief</div>
      <div class="product-ingredients">Menthol, CBD, Turmeric &amp; Magnesium</div>
      <div class="product-size">1 fl oz</div>
    </div>

    <div class="contact contact-phone">CONTACT: 000 123456</div>
    <div class="contact contact-address">Location : 41B, Harbor Lane, Fairhaven,<br>CA90021 USA</div>

    <div class="band-blue"></div>
    <div class="band-white"></div>
    <div class="photo photo-spices" role="img" aria-label="Glass jars of dried herbs, bay leaves, allspice, paprika and ground spices on grey wood"></div>

    <div class="title-box">ALTERNATIVE<br><span class="accent">MEDICINE</span></div>
  </section>
</body>
</html>
```